Harborline Stay Collective Business Card Design

Design a business card for Harborline Stay Collective. Look at the website for colors and reference. Card should have logo, name, title, office number, mobile number, email, URL and a tagline like, "Luxury Hotel & Resort Email Marketing" (This might change).

https://www.harborlinestaycollective.net

The rest I will leave up to your imagination.

Contact Information for Business Card

Logo, name, title, office number, mobile number, email, URL and a tagline like, "Luxury Hotel & Resort Email Marketing" (This might change).

```html
<!DOCTYPE html>
<html lang="en">
<head>
<meta charset="UTF-8">
<title>Harborline Stay Collective – Business Card</title>
<link href="https://fonts.googleapis.com/css2?family=Arimo:wght@400;700&display=swap" rel="stylesheet">
<style>
  :root {
    --stage: #7b7b7b;
    --paper: #f4f4f5;
    --ink: #0a0a0a;
    --accent: #f07a12;
    --light-text: #ffffff;
  }
  * { margin: 0; padding: 0; box-sizing: border-box; }
  html, body { width: 1200px; height: 900px; overflow: hidden; }
  body {
    background: var(--stage);
    font-family: "Arimo", Arial, sans-serif;
    position: relative;
  }
  .card {
    position: absolute;
    width: 560px;
    height: 320px;
    border-radius: 26px;
    overflow: hidden;
  }
  .card-front {
    left: 110px;
    top: 80px;
    background: var(--paper);
    border-bottom: 4px solid var(--accent);
    border-left: 2px solid var(--accent);
    display: flex;
    align-items: center;
    justify-content: center;
  }
  .card-back {
    left: 530px;
    top: 500px;
    background: var(--ink);
    border-bottom: 3px solid var(--paper);
  }
  .wordmark {
    display: flex;
    align-items: center;
    gap: 12px;
    font-weight: 700;
    letter-spacing: 0.02em;
    text-transform: uppercase;
  }
  .wordmark-mark {
    flex: 0 0 auto;
    width: 14px;
    height: 14px;
    background: var(--accent);
  }
  .card-front .wordmark { font-size: 28px; color: var(--ink); }
  .card-back .wordmark {
    position: absolute;
    left: 36px;
    top: 140px;
    width: 220px;
    font-size: 18px;
    line-height: 1.2;
    color: var(--light-text);
  }
  .card-back .wordmark-mark { width: 12px; height: 12px; }
  .contact-block {
    position: absolute;
    left: 285px;
    top: 58px;
    color: var(--light-text);
  }
  .person-name {
    color: var(--accent);
    font-weight: 700;
    font-size: 20px;
  }
  .person-title {
    font-size: 13px;
    margin: 2px 0 16px 12px;
  }
  .contact-list { list-style: none; font-size: 12.5px; line-height: 1.45; white-space: nowrap; }
  .contact-list li { padding-left: 12px; }
  .contact-label { color: var(--accent); font-weight: 700; margin-right: 4px; }
  .tagline {
    position: absolute;
    right: 36px;
    bottom: 34px;
    color: var(--light-text);
    font-size: 14px;
  }
</style>
</head>
<body>
  <section class="card card-front" aria-label="Card front">
    <div class="wordmark">
      <span class="wordmark-mark"></span>
      <span>Harborline Stay Collective</span>
    </div>
  </section>

  <section class="card card-back" aria-label="Card back">
    <div class="wordmark">
      <span class="wordmark-mark"></span>
      <span>Harborline Stay Collective</span>
    </div>
    <div class="contact-block">
      <p class="person-name">Marcus Delane</p>
      <p class="person-title">President</p>
      <ul class="contact-list">
        <li><span class="contact-label">P :</span>555.014.2200</li>
        <li><span class="contact-label">C :</span>555.014.2201</li>
        <li><span class="contact-label">E :</span>info@harborlinestaycollective.net</li>
        <li><span class="contact-label">W :</span>www.harborlinestaycollective.net</li>
      </ul>
    </div>
    <p class="tagline">Luxury Hotel &amp; Resort Email Marketing</p>
  </section>
</body>
</html>
```